Coin Laundry machine instructions

Looking to make 2 posters for laundry instructions on how to use the machines. Which will fit inside a 8-1/2x11 frame with the writing inset 1" inch from all edges.
Needed 1 for waher:
Laundry Room Instructions
Top Load Washer
1. Add the amount of detergent recommended.
2. insert coins as indicated.
3.Load clothes evenly and loosely. Do not over stuff.
4. Follow the operating instructions on the washer and select the temp and fabric selector knob.

For Service Call: Harbor Spinwell 626-318-5907

Needed 1 for Dryer:
Laundry Room Instructions
Dryer
1. Clean the lint filter.
2. Place clothes loosely in the dryer and do not over stuff.
3. Insert coins as indicated.
4. To start the dryer, select a fabric setting. Press start.
5. Remove delicate and permanent press articles promptly after the drying cycle to avoid wrinkling.

Target Market(s)

Coin Laundry

Requirements
Must have
• inset of writing and pictures 1" from all edges so the picture frame won't cover any writing

```html
<!DOCTYPE html>
<html lang="en">
<head>
<meta charset="utf-8">
<title>Laundry Room Instructions Posters</title>
<link href="https://fonts.googleapis.com/css2?family=Nunito+Sans:wght@400;600;800&display=swap" rel="stylesheet">
<style>
  :root{
    --page:#f2f2f2;
    --washer-deep:#1f3f9a;
    --washer-mid:#1f6fd6;
    --washer-light:#3fb8f0;
    --washer-text:#1e3fa8;
    --dryer-deep:#1e8a4a;
    --dryer-mid:#4fb84a;
    --dryer-light:#9ed84a;
    --dryer-text:#1f9a62;
    --dryer-title:#8cc63f;
    --white:#ffffff;
  }
  *{box-sizing:border-box;margin:0;padding:0}
  html,body{width:1200px;height:877px;overflow:hidden;background:var(--page)}
  body{font-family:"Nunito Sans",sans-serif;position:relative}
  .poster{position:absolute;top:68px;width:572px;height:740px;overflow:hidden}
  .poster--washer{left:16px}
  .poster--dryer{left:612px}
  .backdrop{position:absolute;inset:0}
  .poster--washer .backdrop{background:radial-gradient(ellipse at 45% 50%,#ffffff 0%,#ffffff 38%,#8fd3f5 62%,var(--washer-mid) 85%,var(--washer-deep) 100%)}
  .poster--dryer .backdrop{background:radial-gradient(ellipse at 45% 50%,#ffffff 0%,#f4fbe9 38%,#bfe383 62%,var(--dryer-mid) 88%,var(--dryer-deep) 100%)}
  .header{position:absolute;top:70px;left:0;width:520px;height:82px;background:linear-gradient(90deg,#fff 0%,#fff 80%,rgba(255,255,255,0) 100%);text-align:center;padding-top:10px;padding-right:40px}
  .header__kicker{font-size:22px;font-weight:400;line-height:1.05}
  .header__title{font-size:34px;font-weight:800;line-height:1.05}
  .poster--washer .header__kicker{color:var(--washer-light)}
  .poster--washer .header__title{color:var(--washer-text)}
  .poster--dryer .header__kicker{color:#4a8a62}
  .poster--dryer .header__title{color:var(--dryer-title)}
  .illustration{position:absolute;left:92px;width:108px;height:108px;border-radius:50%}
  .poster--washer .illustration{background:radial-gradient(circle at 40% 35%,#4a7fe0,var(--washer-deep))}
  .poster--dryer .illustration{background:radial-gradient(circle at 40% 35%,#5fb99a,#2d8a6a)}
  .step{position:absolute;left:200px;width:300px;text-align:center;font-size:17px;line-height:1.25}
  .poster--washer .step{color:var(--washer-text)}
  .poster--dryer .step{color:var(--dryer-text)}
  .step--wide{left:40px;width:480px}
  .marker{display:block;margin:0 auto 8px;width:56px;height:40px}
  .marker text{font-size:17px;font-weight:800;fill:#fff;text-anchor:middle}
  .footer{position:absolute;left:0;right:0;top:672px;height:44px;color:var(--white);font-size:16px;text-align:center;line-height:44px}
  .poster--washer .footer{background:var(--washer-deep)}
  .poster--dryer .footer{background:linear-gradient(90deg,#2aa64a,#4cc24a,#2aa64a)}
  .footer strong{font-weight:800}
</style>
</head>
<body>
<section class="poster poster--washer">
  <div class="backdrop" role="img" aria-label="Blue water droplet photo background"></div>
  <header class="header">
    <p class="header__kicker">Laundry Room Instructions</p>
    <h1 class="header__title">Top Load Washer</h1>
  </header>
  <div class="illustration" style="top:168px" role="img" aria-label="Hand pouring detergent into washer"></div>
  <div class="illustration" style="top:290px" role="img" aria-label="Hand inserting coins into slot"></div>
  <div class="illustration" style="top:410px" role="img" aria-label="Loading clothes into top load washer"></div>
  <div class="illustration" style="top:540px" role="img" aria-label="Finger selecting fabric setting button"></div>
  <div class="step" style="top:168px"><svg class="marker" viewBox="0 0 56 40"><polygon points="0,0 56,0 28,40" fill="var(--washer-light)"/><text x="28" y="22">1</text></svg>Add the amount<br>of detergent<br>recommended.</div>
  <div class="step" style="top:292px"><svg class="marker" viewBox="0 0 56 40"><polygon points="0,0 56,0 28,40" fill="var(--washer-light)"/><text x="28" y="22">2</text></svg>Insert coins<br>as indicated.</div>
  <div class="step" style="top:400px;left:180px;width:340px"><svg class="marker" viewBox="0 0 56 40"><polygon points="0,0 56,0 28,40" fill="var(--washer-light)"/><text x="28" y="22">3</text></svg>Load clothes evenly<br>and loosely. Do not over stuff.</div>
  <div class="step" style="top:505px"><svg class="marker" viewBox="0 0 56 40"><polygon points="0,0 56,0 28,40" fill="var(--washer-light)"/><text x="28" y="22">4</text></svg>Follow the operating<br>instructions on the washer<br>and select the temp<br>and fabric selector knob.</div>
  <footer class="footer">For Service Call: <strong>Harbor Spinwell 626-318-5907</strong></footer>
</section>

<section class="poster poster--dryer">
  <div class="backdrop" role="img" aria-label="Green grass photo background"></div>
  <header class="header">
    <p class="header__kicker">Laundry Room Instructions</p>
    <h1 class="header__title">Dryer</h1>
  </header>
  <div class="illustration" style="top:155px" role="img" aria-label="Hand cleaning dryer lint filter"></div>
  <div class="illustration" style="top:265px" role="img" aria-label="Clothes placed loosely in dryer"></div>
  <div class="illustration" style="top:372px" role="img" aria-label="Hand inserting coins into slot"></div>
  <div class="illustration" style="top:476px" role="img" aria-label="Finger selecting fabric setting button"></div>
  <div class="step" style="top:155px"><svg class="marker" viewBox="0 0 56 40"><polygon points="0,0 56,0 28,40" fill="#9fe0c0"/><text x="28" y="22">1</text></svg>Clean the lint filter.</div>
  <div class="step" style="top:240px;left:170px;width:360px"><svg class="marker" viewBox="0 0 56 40"><polygon points="0,0 56,0 28,40" fill="#6fcf9f"/><text x="28" y="22">2</text></svg>Place clothes loosely in<br>the dryer and do not over stuff.</div>
  <div class="step" style="top:343px"><svg class="marker" viewBox="0 0 56 40"><polygon points="0,0 56,0 28,40" fill="#3fbf85"/><text x="28" y="22">3</text></svg>Insert coins<br>as indicated.</div>
  <div class="step" style="top:444px"><svg class="marker" viewBox="0 0 56 40"><polygon points="0,0 56,0 28,40" fill="#25ad6f"/><text x="28" y="22">4</text></svg>To start the dryer,<br>select a fabric setting.<br>Press start.</div>
  <div class="step step--wide" style="top:565px;font-size:18px"><svg class="marker" viewBox="0 0 56 40"><polygon points="0,0 56,0 28,40" fill="var(--dryer-deep)"/><text x="28" y="22">5</text></svg>Remove delicate and permanent press articles<br>promptly after the drying cycle to avoid wrinkling.</div>
  <footer class="footer">For Service Call: <strong>Harbor Spinwell 626-318-5907</strong></footer>
</section>
</body>
</html>
```